Harborline Crest Insurance Services

we are a high end insurance agency we specialize on Auto | Home | Business | Life looking for something professional and luxuries at the same time. if you guys need anything else please let me know.

Auto | Home | Business | Life must be under logo on the back with black background.

i want the back part to be black with our gold logo on it.

Target Market(s)

Auto | Home | Business | Life

Industry/Entity Type

Insurance Broker

Contact Information for Business Card

My logo is gold so a black in the back would be nice.

Font styles to use
Serif

Colors
000000

Requirements
Must have
• Big logo on the back with black background.

```html
<!DOCTYPE html>
<html lang="en">
<head>
<meta charset="utf-8">
<title>Harborline Crest Insurance Services – Business Card</title>
<link rel="stylesheet" href="https://fonts.googleapis.com/css2?family=Cinzel:wght@600&family=Lato:wght@400;700&display=swap">
<style>
  :root {
    --canvas-bg: #e8e6e3;
    --card-black: #000000;
    --card-white: #fbfbfb;
    --brand-gold: #dcae2e;
    --accent-yellow: #f7b900;
    --text-white: #ffffff;
    --text-silver: #c4c4c4;
    --rule-grey: #8a8a8a;
  }
  * { margin: 0; padding: 0; box-sizing: border-box; }
  html, body {
    width: 1200px; height: 960px; overflow: hidden;
    background: var(--canvas-bg);
  }
  .canvas { position: relative; width: 1200px; height: 960px; }
  .card {
    position: absolute; left: 272px; width: 663px; height: 380px;
    overflow: hidden;
  }
  .card--front { top: 73px; background: var(--card-black); }
  .card--back { top: 508px; background: var(--card-black); }

  .wordmark {
    position: absolute; text-align: center;
    font-family: "Cinzel", serif; font-weight: 600;
    color: var(--brand-gold); line-height: 1.15;
  }
  .wordmark__name { display: block; font-size: 44px; letter-spacing: 1px; }
  .wordmark__sub { display: block; font-size: 21px; letter-spacing: 6px; margin-top: 8px; }
  .card--front .wordmark { left: 0; right: 0; top: 128px; }
  .card--back .wordmark { left: 8px; width: 304px; top: 148px; }
  .card--back .wordmark__name { font-size: 28px; }
  .card--back .wordmark__sub { font-size: 14px; letter-spacing: 3px; margin-top: 6px; }

  .service-line {
    display: block; margin-top: 20px;
    font-family: "Lato", sans-serif; font-weight: 400;
    font-size: 15px; letter-spacing: 4px;
    color: var(--text-silver);
  }

  .back-split { position: absolute; inset: 0; width: 663px; height: 380px; }

  .contact {
    position: absolute; left: 377px; top: 82px;
    font-family: "Lato", sans-serif; color: var(--text-white);
  }
  .contact__name {
    font-weight: 700; font-size: 20px; letter-spacing: 2px;
    color: var(--accent-yellow); line-height: 24px;
  }
  .contact__role { font-size: 15px; letter-spacing: 1.5px; line-height: 18px; }
  .contact__rule {
    width: 176px; height: 1px; background: var(--rule-grey);
    margin: 13px 0 12px;
  }
  .contact__rule--end { margin: 6px 0 0; }
  .contact__address { font-size: 15px; letter-spacing: 1.3px; line-height: 20px; }
  .contact__list { list-style: none; margin-top: 16px; }
  .contact__item {
    display: flex; align-items: center; gap: 4px;
    font-size: 15px; letter-spacing: 1.2px; line-height: 21px;
  }
  .contact__icon { width: 13px; height: 13px; fill: var(--accent-yellow); flex: none; }
</style>
</head>
<body>
<main class="canvas">

  <section class="card card--front" aria-label="Card front">
    <div class="wordmark">
      <span class="wordmark__name">Harborline Crest</span>
      <span class="wordmark__sub">Insurance Services</span>
      <span class="service-line">AUTO | HOME | BUSINESS | LIFE</span>
    </div>
  </section>

  <section class="card card--back" aria-label="Card back">
    <svg class="back-split" viewBox="0 0 663 380" aria-hidden="true">
      <polygon points="0,0 376,0 293,380 0,380" fill="var(--card-white)"/>
      <polygon points="376,0 382,0 307,380 293,380" fill="var(--accent-yellow)"/>
    </svg>

    <div class="wordmark">
      <span class="wordmark__name">Harborline Crest</span>
      <span class="wordmark__sub">Insurance Services</span>
    </div>

    <div class="contact">
      <p class="contact__name">MARISA HOLLOWAY</p>
      <p class="contact__role">Director</p>
      <div class="contact__rule"></div>
      <p class="contact__address">4725 Larkfield Ave<br>Westbrook, CA 91420</p>
      <div class="contact__rule contact__rule--end"></div>
      <ul class="contact__list">
        <li class="contact__item">
          <svg class="contact__icon" viewBox="0 0 16 16" aria-hidden="true"><path d="M3.6 1l2.3 3.2-1.4 1.7c.9 2 2.6 3.7 4.6 4.6l1.7-1.4L14 11.4 12.6 14C6.6 14 2 9.4 2 3.4z"/></svg>
          <span>(818) 555-0148</span>
        </li>
        <li class="contact__item">
          <svg class="contact__icon" viewBox="0 0 16 16" aria-hidden="true"><path d="M4.5 0h7A1.5 1.5 0 0 1 13 1.5v13a1.5 1.5 0 0 1-1.5 1.5h-7A1.5 1.5 0 0 1 3 14.5v-13A1.5 1.5 0 0 1 4.5 0zM4.8 2v10.5h6.4V2zM8 13.2a.9.9 0 1 0 0 1.8.9.9 0 0 0 0-1.8z"/></svg>
          <span>(800) 555-0192</span>
        </li>
        <li class="contact__item">
          <svg class="contact__icon" viewBox="0 0 16 16" aria-hidden="true"><path d="M1 3h14v1.2L8 8.8 1 4.2zM1 5.8l7 4.6 7-4.6V13H1z"/></svg>
          <span>harborlinecrest@mail.com</span>
        </li>
        <li class="contact__item">
          <svg class="contact__icon" viewBox="0 0 16 16" aria-hidden="true"><path d="M8 1a7 7 0 1 0 0 14A7 7 0 0 0 8 1zm-.7 1.6v2.6H5.2c.5-1.4 1.2-2.3 2.1-2.6zm1.4 0c.9.3 1.6 1.2 2.1 2.6H8.7zM4.8 2.9c-.4.6-.8 1.4-1 2.3H2.7a5.6 5.6 0 0 1 2.1-2.3zm6.4 0a5.6 5.6 0 0 1 2.1 2.3h-1.1c-.2-.9-.6-1.700-1-2.3zM2.5 6.5h1.1a12 12 0 0 0 0 3H2.5a5.6 5.6 0 0 1 0-3zm2.5 0h2.3v3H5a10 10 0 0 1 0-3zm3.7 0H11a10 10 0 0 1 0 3H8.7zm3.7 0h1.1a5.6 5.6 0 0 1 0 3h-1.1a12 12 0 0 0 0-3zM2.7 10.8h1.1c.2.9.6 1.7 1 2.3a5.6 5.6 0 0 1-2.1-2.3zm2.5 0h2.1v2.6c-.9-.3-1.6-1.2-2.1-2.6zm3.5 0h2.1c-.5 1.4-1.2 2.3-2.1 2.6zm3.5 0h1.1a5.6 5.6 0 0 1-2.1 2.3c.4-.6.8-1.4 1-2.3z"/></svg>
          <span>www.harborlinecrest.com</span>
        </li>
      </ul>
    </div>
  </section>

</main>
</body>
</html>
```